Funeral Services Web Site

We need a website for a Funeral Services company. The choice of colors is free of charge. One Page Website with 8 sections. Menu: - Home - Our Services - Obituaries -> link to another page. - Our Shop - Funeral Monument - Funeral Contract - Contact Us

Target Market(s)

Every one need Funeral Services

Coding

Coded - Design and coding required

Number of Pages Required

2 page

Font styles to use
Sans Serif
Script

Colors

Designer to choose colors to be used in the design.

```html
<!DOCTYPE html>
<html lang="en">
<head>
<meta charset="utf-8">
<title>Marchal &amp; Devos – Funeral Services</title>
<link href="https://fonts.googleapis.com/css2?family=Baumans&family=Lato:wght@300;400;700&display=swap" rel="stylesheet">
<style>
:root{
  --brown:#7b6a56;
  --brown-dark:#6b5a48;
  --plan:#8b8176;
  --plan-main:#7b6552;
  --ink:#333;
  --muted:#8a8a8a;
  --light:#f1f1f1;
  --footer:#2a2623;
  --white:#fff;
}
*{box-sizing:border-box;margin:0;padding:0}
html,body{width:1200px;height:3846px;overflow:hidden}
body{position:relative;background:var(--white);font-family:'Lato',sans-serif;color:var(--ink)}
.abs{position:absolute}
.heading{font-family:'Baumans',sans-serif;color:var(--brown);font-weight:400;text-align:center;width:100%;font-size:29px;letter-spacing:.3px}
.section-mark{width:38px;height:38px;border-radius:50%;border:3px solid #9c9189;left:581px}
.pill-btn{display:flex;align-items:center;background:var(--brown);color:#fff;border-radius:22px;font-size:14px;font-weight:700;height:36px}
.pill-btn .ico{width:36px;height:36px;border-radius:50%;background:#ece8e3;border:2px solid var(--brown);display:flex;align-items:center;justify-content:center;flex:none}
.pill-btn span{padding:0 18px 0 14px}
/* header */
.phone-pill{left:142px;top:30px;width:146px;height:32px;border-radius:16px;background:var(--brown);color:#fff;font-size:13px;display:flex;align-items:center}
.phone-pill .ico{width:32px;height:32px;border-radius:50%;background:#5f5142;display:flex;align-items:center;justify-content:center;margin-right:12px}
.logo-box{left:505px;top:0;width:192px;height:116px;background:#fff;border-radius:0 0 6px 6px;box-shadow:0 3px 8px rgba(0,0,0,.18);z-index:3;padding:16px 20px}
.logo-sub{font-size:10px;color:var(--brown-dark)}
.logo-row{display:flex;align-items:center;gap:8px;margin-top:6px}
.logo-name{font-size:22px;font-weight:700;color:var(--brown-dark);line-height:1.05}
.logo-dot{width:34px;height:34px;border-radius:50%;background:#cfc8c0;flex:none}
.lang{left:910px;top:30px;width:90px;height:32px;border:1px solid #ccc;border-radius:16px;font-size:13px;color:#888;display:flex;align-items:center;justify-content:center}
.menu-btn{left:1026px;top:30px;width:32px;height:32px;border-radius:50%;background:var(--brown);display:flex;flex-direction:column;align-items:center;justify-content:center;gap:3px}
.menu-btn i{display:block;height:2px;background:#fff;width:12px}
/* hero */
.hero{left:0;top:96px;width:1200px;height:600px;background:linear-gradient(100deg,#e8e2dc 0%,#cfc4b8 35%,#6d5a4a 60%,#2d2420 100%)}
.hero h1{font-family:'Baumans',sans-serif;font-weight:400;color:#fff;font-size:34px;left:142px;top:272px;text-shadow:0 2px 6px rgba(0,0,0,.55)}
.hero p{left:142px;top:322px;font-size:17px;color:#222;line-height:25px;width:430px}
.hero-btn{left:142px;top:393px;width:146px;height:42px;border-radius:21px;background:var(--brown);color:#fff;font-size:17px;font-weight:700;display:flex;align-items:center;justify-content:center;box-shadow:0 3px 6px rgba(0,0,0,.3)}
/* services */
.tile{background:#fff;border:1px solid #e6e6e6;padding:6px}
.tile .ph{width:100%;height:100%;position:relative;display:flex;align-items:flex-end;justify-content:center}
.tile .cap{color:#fff;font-size:14px;text-align:center;line-height:20px;padding-bottom:12px;text-shadow:0 1px 3px rgba(0,0,0,.7)}
/* obituaries */
.obit{width:158px;text-align:center}
.obit .ph{width:158px;height:174px;border:4px solid #fff;box-shadow:0 0 0 1px #e2e2e2}
.obit .name{font-size:14px;color:#444;margin-top:16px}
.obit .date{font-size:12px;color:var(--muted);margin-top:8px}
.obit .place{font-size:11px;color:var(--muted);margin-top:4px}
/* shop */
.shop{left:0;top:1810px;width:1200px;height:318px;background:linear-gradient(90deg,#ececec,#fbfbfb 45%,#e9e9e9)}
.shop h2{font-family:'Baumans',sans-serif;font-weight:400;color:var(--brown);font-size:28px;left:142px;top:68px}
.shop p{left:142px;top:116px;width:440px;font-size:14px;line-height:21px;color:#444}
/* monument */
.mon{position:absolute}
.mon .cap{position:absolute;left:20px;bottom:24px;color:#fff}
.view-all{background:#8c7d68;color:#fff;display:flex;flex-direction:column;align-items:center;justify-content:center;gap:12px;font-size:15px}
/* contract */
.plan{background:#fff;box-shadow:0 0 10px rgba(0,0,0,.14);text-align:center}
.plan .head{background:var(--plan);color:#fff;display:flex;flex-direction:column;align-items:center;justify-content:center;gap:8px;font-size:27px;font-weight:700}
.plan .head .mk{width:36px;height:36px;border-radius:50%;border:3px solid rgba(255,255,255,.55)}
.plan .price{font-size:22px;color:var(--brown-dark);font-weight:700;margin-top:22px}
.plan .off{font-size:14px;color:var(--muted);margin-top:2px}
.plan ul{list-style:none;margin:16px 34px 0;text-align:left;font-size:12px;color:#333}
.plan li{height:33px;line-height:33px;border-bottom:1px solid #eee}
.plan li:last-child{border-bottom:none}
.plan .pill-btn{margin:18px auto 0;width:150px;height:34px;font-size:14px}
.plan .pill-btn .ico{width:34px;height:34px}
.plan-main .head{background:var(--plan-main)}
/* footer */
.footer{left:0;top:3492px;width:1200px;height:354px;background:var(--footer);color:#ddd}
.footer h4{font-size:14px;font-weight:700;color:#fff}
.footer ul{list-style:none;font-size:12px}
.footer li{height:24px;padding-left:14px;position:relative}
.footer li::before{content:"›";position:absolute;left:0;top:-2px;color:#aaa}
.contact-line{display:flex;gap:14px;font-size:12px;line-height:18px}
.footer .copy{left:142px;top:318px;font-size:12px;color:#ccc}
.social{width:12px;height:12px;border-radius:50%;background:#999}
</style>
</head>
<body>

<!-- Header -->
<header>
  <div class="abs phone-pill"><span class="ico"><svg width="14" height="14" viewBox="0 0 24 24"><path fill="#fff" d="M6.6 10.8a15 15 0 006.6 6.6l2.2-2.2c.3-.3.7-.4 1-.2 1.1.4 2.3.6 3.6.6.6 0 1 .4 1 1V20c0 .6-.4 1-1 1A17 17 0 013 4c0-.6.4-1 1-1h3.5c.6 0 1 .4 1 1 0 1.3.2 2.5.6 3.6.1.3 0 .7-.2 1z"/></svg></span>071/246810</div>
  <div class="abs logo-box">
    <div class="logo-sub">Pompes funèbres</div>
    <div class="logo-row"><div class="logo-name">Marchal<br>&amp; Devos</div><div class="logo-dot"></div></div>
  </div>
  <div class="abs lang">English&nbsp;<svg width="8" height="6" viewBox="0 0 8 6"><path d="M1 1l3 3 3-3" stroke="#888" fill="none"/></svg></div>
  <div class="abs menu-btn"><i></i><i style="width:9px;margin-left:-3px"></i><i></i></div>
</header>

<!-- Hero -->
<section class="abs hero" role="img" aria-label="Funeral director comforting a grieving family beside a casket">
  <svg class="abs" style="left:0;top:470px" width="1200" height="130" viewBox="0 0 1200 130" preserveAspectRatio="none">
    <path d="M0 70 C150 20 320 10 470 40 C640 75 760 110 920 95 C1040 84 1130 60 1200 52 L1200 130 L0 130Z" fill="#fff"/>
    <path d="M0 70 C150 20 320 10 470 40 C640 75 760 110 920 95 C1040 84 1130 60 1200 52" stroke="#4a3a2e" stroke-width="6" fill="none"/>
  </svg>
</section>
<div class="hero">
</div>
<h1 class="abs" style="font-family:'Baumans',sans-serif;font-weight:400;color:#fff;font-size:34px;left:142px;top:272px;text-shadow:0 2px 6px rgba(0,0,0,.55)">Helping You Cope With Grief</h1>
<p class="abs" style="left:142px;top:322px;font-size:17px;color:#222;line-height:25px;width:430px">We Explain Some of The Feelings You May Have And Suggest Ways of Dealing With Them</p>
<a class="abs hero-btn">Contact Now</a>

<!-- Our Services -->
<section>
  <div class="abs section-mark" style="top:738px"></div>
  <h2 class="abs heading" style="top:785px">Our Services</h2>
  <div class="abs tile" style="left:142px;top:847px;width:289px;height:169px"><div class="ph" role="img" aria-label="Two hands holding in comfort" style="background:linear-gradient(135deg,#e9d3c2,#a8765a 70%,#5b3d2c)"><div class="cap">Personalized and dignified<br>support from the first moments</div></div></div>
  <div class="abs tile" style="left:142px;top:1036px;width:289px;height:169px"><div class="ph" role="img" aria-label="Elderly couple meeting an adviser" style="background:linear-gradient(135deg,#d8d4cf,#8d8277 65%,#4c443d)"><div class="cap">Assistance In All Administrative<br>Procedures</div></div></div>
  <div class="abs tile" style="left:455px;top:847px;width:290px;height:358px"><div class="ph" role="img" aria-label="Smiling young family outdoors" style="background:linear-gradient(170deg,#e8e4dc,#c6b69a 45%,#5a4c3e)"><div class="cap">Death and funeral insurance<br>relieve your loved ones</div></div></div>
  <div class="abs tile" style="left:769px;top:847px;width:289px;height:169px"><div class="ph" role="img" aria-label="Red rose resting on piano keys" style="background:linear-gradient(135deg,#2a2a2a,#6a6a6a 45%,#b8262a 70%,#1c1c1c)"><div class="cap">Offer him his song to<br>pay him a last tribute</div></div></div>
  <div class="abs tile" style="left:769px;top:1036px;width:289px;height:169px"><div class="ph" role="img" aria-label="Orange sunset over the sea" style="background:linear-gradient(180deg,#f0a040,#e56a1d 55%,#6a2610)"><div class="cap">Put down your last wishes to<br>guarantee their respect!</div></div></div>
</section>

<!-- Recent Obituaries -->
<section>
  <div class="abs section-mark" style="top:1292px"></div>
  <h2 class="abs heading" style="top:1338px">Recent Obituaries</h2>
  <div class="abs obit" style="left:145px;top:1397px"><div class="ph" role="img" aria-label="Portrait photo" style="background:linear-gradient(160deg,#c9c5a8,#a2846e)"></div><div class="name">Marco BELLINI</div><div class="date">Apr 23, 2019</div><div class="place">Valmont</div></div>
  <div class="abs obit" style="left:332px;top:1397px"><div class="ph" role="img" aria-label="Portrait photo" style="background:linear-gradient(160deg,#6a5a48,#b08a70 60%,#3e4a68)"></div><div class="name">Pascal RENARD</div><div class="date">Apr 12, 2019</div><div class="place">Bois-lez-Romay</div></div>
  <div class="abs obit" style="left:520px;top:1397px"><div class="ph" role="img" aria-label="Portrait photo" style="background:linear-gradient(160deg,#b9aea2,#c79a8c 60%,#8a5a58)"></div><div class="name">Mireille DUPONT</div><div class="date">Apr 09, 2019</div><div class="place">Florval</div></div>
  <div class="abs obit" style="left:707px;top:1397px"><div class="ph" role="img" aria-label="Placeholder portrait" style="background:#e4e4e4"></div><div class="name">Henri LAMBOT</div><div class="date">Apr 08, 2019</div><div class="place">Montreuil-Haut</div></div>
  <div class="abs obit" style="left:895px;top:1397px"><div class="ph" role="img" aria-label="White calla lilies on black" style="background:linear-gradient(135deg,#0c0c0c,#3c4a2c 50%,#e6e6e0 80%,#111)"></div><div class="name">Sylvie MOREAU</div><div class="date">Apr 05, 2019</div><div class="place">Lessines-Bas</div></div>
  <a class="abs pill-btn" style="left:390px;top:1698px;width:193px"><span class="ico"><svg width="16" height="16" viewBox="0 0 24 24"><circle cx="12" cy="12" r="8" stroke="#7b6a56" stroke-width="2" fill="none"/></svg></span><span>View All Obituaries</span></a>
  <a class="abs pill-btn" style="left:615px;top:1698px;width:197px"><span class="ico"><svg width="16" height="14" viewBox="0 0 24 18"><rect x="2" y="2" width="20" height="14" stroke="#7b6a56" stroke-width="2" fill="none"/><path d="M2 2l10 8 10-8" stroke="#7b6a56" stroke-width="2" fill="none"/></svg></span><span>Get Obituary Alerts</span></a>
</section>

<!-- Our Shop -->
<section class="abs shop">
  <h2 class="abs">Our Shop</h2>
  <p class="abs">Lorem ipsum dolor sit amet, consectetuer adipiscing elit, sed diam no nummy nibh euismod tincidunt ut laoreet dolore magna aliquam volutpat.&nbsp; Ut wisi enim ad minim veniam, quis nostrud</p>
  <a class="abs pill-btn" style="left:142px;top:208px;width:154px"><span class="ico"><svg width="14" height="14" viewBox="0 0 24 24"><path d="M4 6h16l-2 10H6z" fill="#7b6a56"/></svg></span><span>Shop Now</span></a>
  <div class="abs" role="img" aria-label="Bouquet of pink roses in a basket" style="left:700px;top:0;width:440px;height:318px;background:radial-gradient(ellipse at 50% 50%,#c43a64 0%,#9d2a4c 35%,#3f6a32 60%,rgba(240,240,240,0) 72%)"></div>
</section>

<!-- Funeral Monument -->
<section>
  <div class="abs section-mark" style="top:2212px"></div>
  <h2 class="abs heading" style="top:2257px">Funeral Monument</h2>
  <div class="mon" role="img" aria-label="Ornate marble tomb with mourning angel sculpture" style="left:127px;top:2338px;width:289px;height:334px;background:linear-gradient(160deg,#b9ab90,#7c6e58 55%,#3c3428)">
    <div class="cap"><div style="font-size:17px">Lorem ipsum dolor</div><div style="font-size:11px;margin-top:6px;line-height:16px">Lorem ipsum dolor sit amet, consect<br>etu er adipiscing elit, sed diam no</div></div>
  </div>
  <div class="mon" role="img" aria-label="Black granite arched headstone" style="left:424px;top:2338px;width:185px;height:162px;background:linear-gradient(180deg,#6d8c4e,#2a2a2c 55%,#5a7a40)"></div>
  <div class="mon" role="img" aria-label="Black granite double headstone" style="left:424px;top:2510px;width:185px;height:162px;background:linear-gradient(180deg,#6b7a58,#1f1f22 45%,#3a3a3c)"></div>
  <div class="mon" role="img" aria-label="Tall classical granite monument" style="left:618px;top:2338px;width:234px;height:334px;background:linear-gradient(180deg,#d8d6d2,#b0aca4 50%,#8e8a82)"></div>
  <div class="mon" role="img" aria-label="Heart-shaped granite headstone" style="left:861px;top:2338px;width:184px;height:215px;background:linear-gradient(180deg,#4a4442,#7a7672 55%,#8aa070)"></div>
  <a class="mon view-all" style="left:861px;top:2562px;width:184px;height:110px">
    <svg width="24" height="30" viewBox="0 0 24 30"><path d="M3 28V8a9 9 0 0118 0v20z" fill="#fff"/><path d="M12 7v12M8 11h8" stroke="#8c7d68" stroke-width="2"/></svg>
    View All
  </a>
</section>

<!-- Funeral Contract -->
<section>
  <div class="abs section-mark" style="top:2760px"></div>
  <h2 class="abs heading" style="top:2806px">Funeral Contract</h2>
  <div class="abs plan" style="left:157px;top:2895px;width:283px;height:473px">
    <div class="head" style="height:112px"><div class="mk"></div>Plan 1</div>
    <div class="price">$2300</div><div class="off">($50 online discount)</div>
    <ul><li>$ 500.00 Advice &amp; guidance on all funeral</li><li>$ 800.00 Cremation or Burial</li><li>$ 400.00 The coffin</li><li>$ 200.00 Service at local crematorium</li><li>$ 400.00 Full listing of floral tributes</li><li>$ 000.00 Free cancellation period</li></ul>
    <a class="pill-btn"><span class="ico"><svg width="12" height="10" viewBox="0 0 12 10"><path d="M1 1l4 4-4 4M6 1l4 4-4 4" stroke="#7b6a56" stroke-width="1.6" fill="none"/></svg></span><span>Get Started</span></a>
  </div>
  <div class="abs plan plan-main" style="left:450px;top:2875px;width:300px;height:515px;z-index:2">
    <div class="head" style="height:118px"><div class="mk"></div>Plan 2</div>
    <div class="price" style="margin-top:32px">$3000</div><div class="off">($50 online discount)</div>
    <ul><li>$ 500.00 Advice &amp; guidance on all funeral</li><li>$ 800.00 Cremation or Burial</li><li>$ 400.00 The coffin</li><li>$ 200.00 Service at local crematorium</li><li>$ 400.00 Full listing of floral tributes</li><li>$ 000.00 Free cancellation period</li></ul>
    <a class="pill-btn" style="margin-top:40px"><span class="ico"><svg width="12" height="10" viewBox="0 0 12 10"><path d="M1 1l4 4-4 4M6 1l4 4-4 4" stroke="#7b6a56" stroke-width="1.6" fill="none"/></svg></span><span>Get Started</span></a>
  </div>
  <div class="abs plan" style="left:750px;top:2895px;width:293px;height:473px">
    <div class="head" style="height:112px"><div class="mk"></div>Plan 3</div>
    <div class="price">$3500</div><div class="off">($50 online discount)</div>
    <ul><li>$ 500.00 Advice &amp; guidance on all funeral</li><li>$ 800.00 Cremation or Burial</li><li>$ 400.00 The coffin</li><li>$ 200.00 Service at local crematorium</li><li>$ 400.00 Full listing of floral tributes</li><li>$ 000.00 Free cancellation period</li></ul>
    <a class="pill-btn"><span class="ico"><svg width="12" height="10" viewBox="0 0 12 10"><path d="M1 1l4 4-4 4M6 1l4 4-4 4" stroke="#7b6a56" stroke-width="1.6" fill="none"/></svg></span><span>Get Started</span></a>
  </div>
</section>

<!-- Footer -->
<footer class="abs footer">
  <h4 class="abs" style="left:145px;top:72px">Quick Links</h4>
  <ul class="abs" style="left:145px;top:108px">
    <li>Home</li><li>Our Services</li><li>Obituaries</li><li>Our Shop</li><li>Funeral Monument</li><li>Funeral Contract</li><li>Contact Us</li>
  </ul>
  <h4 class="abs" style="left:455px;top:72px">Contact Details</h4>
  <div class="abs contact-line" style="left:455px;top:106px"><svg width="12" height="16" viewBox="0 0 12 16"><path d="M6 0a6 6 0 00-6 6c0 4.5 6 10 6 10s6-5.5 6-10a6 6 0 00-6-6zm0 8.5A2.5 2.5 0 116 3.5a2.5 2.5 0 010 5z" fill="#ddd"/></svg><div>MARCHAL &amp; DEVOS SPRL<br>12 Rue des Tilleuls<br>6500 Valmont, Belgique</div></div>
  <div class="abs contact-line" style="left:455px;top:190px"><svg width="12" height="12" viewBox="0 0 24 24"><path fill="#ddd" d="M6.6 10.8a15 15 0 006.6 6.6l2.2-2.2c.3-.3.7-.4 1-.2 1.1.4 2.3.6 3.6.6.6 0 1 .4 1 1V20c0 .6-.4 1-1 1A17 17 0 013 4c0-.6.4-1 1-1h3.5c.6 0 1 .4 1 1 0 1.3.2 2.5.6 3.6.1.3 0 .7-.2 1z"/></svg><div>071/246810</div></div>
  <div class="abs contact-line" style="left:455px;top:235px"><svg width="13" height="10" viewBox="0 0 24 18"><rect x="1" y="1" width="22" height="16" fill="#ddd"/><path d="M1 1l11 8 11-8" stroke="#2a2623" stroke-width="2" fill="none"/></svg><div>info@marchaldevos.be</div></div>
  <div class="abs" style="left:862px;top:112px;opacity:.6">
    <div style="font-size:10px;color:#ddd">Pompes funèbres</div>
    <div style="display:flex;align-items:center;gap:8px;margin-top:6px"><div style="font-size:26px;font-weight:700;color:#ddd;line-height:1.05">Marchal<br>&amp; Devos</div><div style="width:48px;height:48px;border-radius:50%;background:#999"></div></div>
  </div>
  <div class="abs" style="left:142px;top:296px;width:916px;border-top:1px solid #3d3834"></div>
  <div class="abs copy">Copyright © 2019 MARCHAL &amp; DEVOS SPRL . All Rights Reserved.</div>
  <div class="abs social" style="left:1015px;top:320px" aria-label="Social profile"></div>
  <div class="abs social" style="left:1044px;top:320px" aria-label="Social profile"></div>
</footer>

</body>
</html>
```